General contractor/GM consaltant business card

I need a card for my contracting company in North Dakota, we build industrial buildings for the oil feild and oil feild related companies offices, shops, airplain hangars, airports ext. We have a familly atmosphere on the job and are very relational and personal.
Industry/Entity Type
Industrial
Contact Information for Business Card
Kestrelmoor Builders LLC.
Dwight T.Halvorsun
4736 Quillfern dr. Colorado Springs, CO. 80927
Cell# 406-555-8142
dwight@kestrelmoorbuilders.com

```html
<!DOCTYPE html>
<html lang="en">
<head>
<meta charset="utf-8">
<title>Kestrelmoor Builders LLC. – Business Card</title>
<link rel="stylesheet" href="https://fonts.googleapis.com/css2?family=Fjalla+One&family=Arimo:wght@400&display=swap">
<style>
  :root {
    --page-bg: #e9e9e7;
    --front-dark: #383838;
    --back-grey: #646464;
    --accent-green: #9cc765;
    --accent-green-light: #b9d88f;
    --text-green: #b6dc80;
    --title-grey: #c9c9cf;
  }
  * { margin: 0; padding: 0; box-sizing: border-box; }
  html, body {
    width: 1200px;
    height: 1200px;
    overflow: hidden;
    background: var(--page-bg);
  }
  .sheet {
    width: 1200px;
    height: 1200px;
    display: flex;
    flex-direction: column;
    align-items: center;
    justify-content: center;
    gap: 60px;
  }
  .card {
    position: relative;
    width: 900px;
    height: 514px;
    overflow: hidden;
    box-shadow: 0 6px 18px rgba(0,0,0,0.18);
  }
  .card-art {
    position: absolute;
    inset: 0;
    width: 100%;
    height: 100%;
  }
  .company-name {
    position: absolute;
    top: 62px;
    left: 70px;
    font-family: "Fjalla One", sans-serif;
    font-size: 50px;
    letter-spacing: 0.5px;
    color: var(--title-grey);
  }
  .person-name {
    position: absolute;
    top: 340px;
    left: 70px;
    font-family: "Arimo", sans-serif;
    font-size: 40px;
    color: var(--text-green);
  }
  .contact-list {
    position: absolute;
    left: 70px;
    bottom: 70px;
    list-style: none;
    font-family: "Arimo", sans-serif;
    font-size: 32px;
    line-height: 1.3;
    color: var(--text-green);
  }
</style>
</head>
<body>
<main class="sheet">

  <section class="card card-front" aria-label="Card front">
    <svg class="card-art" viewBox="0 0 900 514" preserveAspectRatio="none" aria-hidden="true">
      <defs>
        <linearGradient id="frontGlow" x1="560" y1="0" x2="900" y2="0" gradientUnits="userSpaceOnUse">
          <stop offset="0" stop-color="#383838"/>
          <stop offset="1" stop-color="#9cc765"/>
        </linearGradient>
      </defs>
      <rect width="900" height="514" fill="url(#frontGlow)"/>
      <path d="M0 0 H570 C610 70 730 250 730 350 C730 455 650 514 560 514 H0 Z" fill="#383838"/>
    </svg>
    <h1 class="company-name">Kestrelmoor Builders LLC.</h1>
    <p class="person-name">Dwight T.Halvorsun</p>
  </section>

  <section class="card card-back" aria-label="Card back">
    <svg class="card-art" viewBox="0 0 900 514" preserveAspectRatio="none" aria-hidden="true">
      <defs>
        <linearGradient id="backGlow" x1="480" y1="0" x2="900" y2="0" gradientUnits="userSpaceOnUse">
          <stop offset="0" stop-color="#646464"/>
          <stop offset="1" stop-color="#b9d88f"/>
        </linearGradient>
      </defs>
      <rect width="900" height="514" fill="url(#backGlow)"/>
      <path d="M0 514 H560 C650 514 730 455 730 360 C730 250 600 130 520 0 H0 Z" fill="#646464"/>
    </svg>
    <ul class="contact-list">
      <li>4736 Quillfern dr. Colorado Springs, CO.</li>
      <li>80927</li>
      <li>Cell# 406-555-8142</li>
      <li>dwight@kestrelmoorbuilders.com</li>
    </ul>
  </section>

</main>
</body>
</html>
```